Larkmoor Stationery Design Project

company name : Larkmoor General Trading LLC.
light watermark taken from the logo to cover almost the middle of the stationary..
logo is attached and an on going business card project is released on the same company name..
thanks
Reason: more time for more designs and to work with comfort..
Industry/Entity Type
Business
Colors
Designer to choose colors to be used in the design.
Look and feel
Each slider illustrates characteristics of the customer's brand and the style your logo design should communicate.

```html
<!DOCTYPE html>
<html lang="en">
<head>
<meta charset="utf-8">
<title>Larkmoor Stationery – Letterhead and Business Card</title>
<link rel="stylesheet" href="https://fonts.googleapis.com/css2?family=Arimo:wght@400;700&display=swap">
<style>
  :root {
    --stage: #2b2b2b;
    --paper: #ffffff;
    --blue-top: #1f66bd;
    --blue-deep: #0b2584;
    --ink: #222222;
    --ink-soft: #666666;
    --brand: #1a4f9c;
    --accent: #1a4f9c;
    --signature-tone: #e3e6ee;
  }
  * { margin: 0; padding: 0; box-sizing: border-box; }
  html, body { width: 872px; height: 1200px; overflow: hidden; }
  body { background: var(--stage); position: relative; font-family: "Arimo", Arial, sans-serif; }

  .letterhead {
    position: absolute; left: 120px; top: 18px; width: 652px; height: 845px;
    background: var(--paper);
  }
  .letterhead__art { position: absolute; left: 0; top: 0; }

  .company-address {
    position: absolute; left: 476px; top: 43px;
    color: #fff; font-weight: 700; font-style: normal; font-size: 10.5px; line-height: 13px;
  }

  .brand-name {
    position: absolute; font-family: "Arimo", Arial, sans-serif; font-weight: 700;
    color: var(--brand); white-space: nowrap;
  }
  .letterhead .brand-name { left: 121px; top: 158px; font-size: 25px; }

  .letter { position: absolute; left: 121px; top: 300px; width: 434px; color: var(--ink); }
  .letter__salutation { color: var(--accent); font-weight: 700; font-size: 11px; margin-bottom: 17px; }
  .letter__body p { font-size: 8.55px; line-height: 16.35px; margin-bottom: 16px; }

  .sign-off { position: absolute; left: 458px; top: 671px; color: var(--ink-soft); }
  .sign-off__closing { font-size: 8px; }
  .sign-off__signature {
    width: 118px; height: 66px; margin: 3px 0 6px -12px;
    background: linear-gradient(135deg, transparent, var(--signature-tone), transparent);
    border-radius: 40%;
  }
  .sign-off__name { font-size: 8px; color: #555; }
  .sign-off__role { font-size: 6.5px; color: #555; margin-top: 2px; }

  .business-card {
    position: absolute; left: 553px; top: 156px; width: 268px; height: 154px;
    box-shadow: -4px 4px 10px rgba(0,0,0,0.45);
    overflow: hidden;
  }
  .business-card__art { position: absolute; left: 0; top: 0; }
  .business-card .brand-name { left: 16px; top: 69px; font-size: 14px; }
  .card-person { position: absolute; left: 168px; top: 67px; color: var(--ink-soft); }
  .card-person__name { font-size: 10px; letter-spacing: 0.3px; }
  .card-person__role { font-size: 5px; color: var(--accent); margin-top: 1px; }
  .card-person__contact { font-size: 5px; line-height: 9px; margin-top: 12px; }
</style>
</head>
<body>

<section class="letterhead" aria-label="Letterhead">
  <svg class="letterhead__art" width="652" height="845" viewBox="0 0 652 845" aria-hidden="true">
    <defs>
      <linearGradient id="letterBlue" x1="0" y1="0" x2="0" y2="1">
        <stop offset="0" stop-color="var(--blue-top)"/>
        <stop offset="1" stop-color="var(--blue-deep)"/>
      </linearGradient>
      <linearGradient id="letterPaperFade" x1="0" y1="0" x2="0" y2="1">
        <stop offset="0.55" stop-color="#ffffff"/>
        <stop offset="1" stop-color="#ececef"/>
      </linearGradient>
    </defs>
    <rect x="12" y="2" width="633" height="830" fill="url(#letterBlue)"/>
    <path d="M12,232 C20,82 180,6 310,4 C440,2 585,215 645,557 L645,832 L180,832 C80,702 20,542 12,362 Z" fill="url(#letterPaperFade)"/>
    <path d="M14,500 C40,650 120,770 210,832 L200,832 C110,775 30,660 14,520 Z" fill="#ffffff"/>
    <path d="M538,285 C590,360 630,460 645,552 L645,575 C625,470 590,370 532,290 Z" fill="#ffffff"/>
  </svg>

  <address class="company-address">
    Company Address:<br>
    Street 2740<br>
    ZIP Code: 3815<br>
    Phone: 412- 306- 7190<br>
    Fax: 412- 306- 7191
  </address>

  <div class="brand-name">Larkmoor Trading</div>

  <article class="letter">
    <p class="letter__salutation">Dear Mr. Hale</p>
    <div class="letter__body">
      <p>Lorem ipsum dolor sit amet, consectetur adipiscing elit. Vestibulum adipiscing felis ac tortor consectetur feugiat. Etiam malesuada sodales eros ut ornare. Sed lorem eros, mattis id pretium ut, faucibus sit amet quam. Nullam consectetur ultricies ipsum, fringilla porttitor erat ornare at. Sed sit amet dui vel sapien ultrices vulputate. In hac habitasse platea dictumst. Nam est nisi, rhoncus at sagittis a, porttitor adipiscing nulla. Vivamus placerat felis ultrices quam iaculis eget dignissim felis egestas. Integer nec molestie lorem. Sed odio tellus, vulputate sed laoreet non, vulputate id justo. Etiam suscipit, odio vel auctor dictum, felis turpis ullamcorper neque, quis sodales risus metus in magna. Morbi pellentesque justo et quam laoreet facilisis. Aenean placerat, urna ornare aliquet tincidunt, lorem justo molestie ligula, id placerat est metus nec lectus. Nullam eu ipsum quis turpis tristique iaculis rutrum nec nibh. Phasellus risus eros, semper sit amet faucibus sit amet, laoreet et neque. Donec eros sem, viverra dictum faucibus quis, ullamcorper tincidunt nulla.</p>
      <p>Aenean ut congue tellus. Class aptent taciti sociosqu ad litora torquent per conubia nostra, per inceptos himenaeos. Sed facilisis, velit tincidunt pharetra fermentum, urna tortor iaculis erat, vitae sollicitudin leo mauris quis mi. Cras malesuada sem ac ipsum sagittis ultrices. Mauris fermentum porttitor nisi, eu facilisis lorem consectetur et. Suspendisse est elit, scelerisque ac euismod id, scelerisque viverra odio. Nullam scelerisque metus in eros semper congue. Fusce a fermentum est. Ut ac leo dolor. Quisque dignissim mauris a neque luctus pretium ultrices risus sagittis. Aenean quam massa, rutrum ac hendrerit eu, interdum eu nulla. Curabitur a velit mauris, sed porta eros. Cras id egestas sapien. Proin non metus eget felis eleifend adipiscing. Nunc malesuada pharetra blandit.</p>
    </div>
  </article>

  <div class="sign-off">
    <p class="sign-off__closing">Your sincerely:</p>
    <div class="sign-off__signature" role="img" aria-label="Handwritten signature"></div>
    <p class="sign-off__name">Ellis Warde</p>
    <p class="sign-off__role">Office Manager</p>
  </div>
</section>

<section class="business-card" aria-label="Business card">
  <svg class="business-card__art" width="268" height="154" viewBox="0 0 268 154" aria-hidden="true">
    <defs>
      <linearGradient id="cardBlue" x1="0" y1="0" x2="0" y2="1">
        <stop offset="0" stop-color="var(--blue-top)"/>
        <stop offset="1" stop-color="var(--blue-deep)"/>
      </linearGradient>
    </defs>
    <rect width="268" height="154" fill="url(#cardBlue)"/>
    <path d="M0,62 C10,20 80,3 170,5 C215,7 250,30 268,50 L268,154 L120,154 C60,148 12,122 0,98 Z" fill="#ffffff"/>
    <path d="M150,8 C200,10 245,30 268,48 L268,52 C240,32 200,14 150,8 Z" fill="#ffffff" opacity="0.6"/>
    <path d="M40,128 C80,146 130,152 170,154 L150,154 C110,150 70,142 40,128 Z" fill="#ffffff"/>
  </svg>
  <div class="brand-name">Larkmoor Trading</div>
  <div class="card-person">
    <p class="card-person__name">DELVANE</p>
    <p class="card-person__role">Graphic designer</p>
    <p class="card-person__contact">
      Street 2740<br>
      ZIP Code: 3815<br>
      Phone: 412- 306- 7190<br>
      Fax: 412- 306- 7191
    </p>
  </div>
</section>

</body>
</html>
```